Welcome Card for first time customers

This card is for LeafHarbor and will be included with the first purchase. We are an online company that deals with cannabis. We want to capture our first time buyers and turn them into life long customers. This card is aimed to show them all the benefits of being a returning a customer with us as well as thanking them for choosing us from our many competitors.

This card will be the same size as a postcard (4 x 6 inches) and needs to be double sided.

*if you need a different format for our logos just ask
**THE WINNER WILL BE ASKED TO COMPLETE FUTURE PROJECTS

Target Market(s)

19+

Industry/Entity Type

Cannabis

Requirements
Must have
• - Welcome phrase: "Welcome to the LHR family"

- space for discount code with second spot for the expiration date underneath. Phrase: "Save 15% off your next purchase"

- Perks of being a part of the family:

1. Loyalty Program "Once you've made 5 orders with us you'll be able to join our Loyalty Program! You’ll receive 2.5% back in points with every order to use towards a future purchase. So go ahead, indulge. You deserve it!"

2. Referral Program "Refer a friend using your customer number and they will receive $25 off their first purchase with us AND you'll also receive $25 for your next purchase! Get the full details and customer number at https://www.leafharbor-shop.example/loyalty/"

- Contact information: Website: leafharbor-shop.example. Phone number: 1-833-555-LEAF. Instagram: leafharbor_nth
Nice to have
• Graphic photo side of the postcard to have a design that really stands out, looking modern and sophisticated with a good use of space and colour. Would love to see use of lifestyle cannabis images or real life images. inspirational photos are attached. Include the welcome phrase on this side.

Text side of postcard to use the space well while including the 2 perks.

```html
<!DOCTYPE html>
<html lang="en">
<head>
<meta charset="utf-8">
<title>LeafHarbor Welcome Card</title>
<link rel="stylesheet" href="https://fonts.googleapis.com/css2?family=Kaushan+Script&family=Kalam:wght@400;700&family=Open+Sans:wght@400;600;700&family=Playfair+Display:ital,wght@1,700&display=swap">
<style>
  :root {
    --stage: #d2b4b5;
    --stage-light: #e4d2d3;
    --white: #ffffff;
    --ink: #111111;
    --charcoal: #222021;
    --green-light: #6cbf86;
    --green-dark: #1d3d2e;
    --leaf-text: #233f2e;
    --magenta: #c2187a;
    --label-red: #ee1565;
    --number-red: #ea1758;
    --cyan: #29c3d0;
    --photo-green: #2e6b22;
    --photo-deep: #16300f;
    --photo-pink: #c24fb0;
    --photo-violet: #7a2d86;
  }
  * { box-sizing: border-box; margin: 0; padding: 0; }
  html, body { width: 1200px; height: 1200px; overflow: hidden; }
  body {
    position: relative;
    background: linear-gradient(180deg, var(--stage) 0%, var(--stage) 55%, var(--stage-light) 100%);
    font-family: "Open Sans", sans-serif;
  }
  .side-label {
    position: absolute;
    font-family: "Playfair Display", serif;
    font-style: italic;
    font-weight: 700;
    font-size: 40px;
    color: var(--label-red);
  }
  .side-label--front { left: 318px; top: 62px; }
  .side-label--back { left: 876px; top: 36px; }

  /* FRONT */
  .card-front {
    position: absolute;
    left: 37px; top: 138px;
    width: 652px; height: 435px;
    background: var(--white);
    overflow: hidden;
  }
  .offer-panel {
    position: absolute; left: 0; top: 0; width: 191px; height: 100%;
  }
  .brand-name {
    font-family: "Open Sans", sans-serif;
    font-weight: 700;
    color: var(--ink);
  }
  .offer-panel .brand-lockup {
    position: absolute; left: 0; width: 191px; top: 58px;
    display: flex; flex-direction: column; align-items: center; gap: 10px;
  }
  .brand-mark { width: 30px; height: 30px; background: var(--ink); }
  .offer-panel .brand-name { font-size: 24px; }
  .offer-headline {
    position: absolute; left: 0; width: 191px; top: 222px;
    text-align: center;
    font-family: "Kaushan Script", cursive;
    font-size: 20px; line-height: 22px; color: var(--ink);
  }
  .pill {
    position: absolute; left: 19px; width: 151px; height: 39px;
    border-radius: 20px;
    background: linear-gradient(135deg, var(--green-light) 0%, #3f8a5f 45%, var(--green-dark) 100%);
    color: var(--white); font-size: 16px; line-height: 39px; padding-left: 19px;
  }
  .pill--code { top: 303px; }
  .pill--date { top: 392px; }
  .valid-label {
    position: absolute; left: 38px; top: 354px;
    font-size: 16px; color: var(--leaf-text);
  }
  .hero {
    position: absolute; left: 191px; top: 0; width: 461px; height: 435px;
  }
  .hero-photo {
    position: absolute; inset: 0;
    background:
      radial-gradient(ellipse at 60% 75%, #e27fd0 0%, transparent 45%),
      linear-gradient(180deg, var(--photo-green) 0%, #3b8a2a 30%, #5a6e3a 48%, var(--photo-pink) 62%, var(--photo-violet) 100%);
  }
  .hero-band { position: absolute; inset: 0; }
  .hero-frame {
    position: absolute; left: 6px; top: 6px; right: 6px; bottom: 6px;
    border: 4px solid var(--white);
  }
  .hero-title {
    position: absolute; left: 0; right: 0; top: 30px;
    text-align: center; color: var(--white);
    font-family: "Kaushan Script", cursive;
  }
  .hero-title .line-1 { display: block; font-size: 48px; line-height: 72px; }
  .hero-title .line-2 { display: block; font-size: 60px; line-height: 90px; }

  /* BACK */
  .card-back {
    position: absolute;
    left: 717px; top: 117px;
    width: 446px; height: 670px;
    background: var(--white);
    overflow: hidden;
  }
  .leaf-pattern {
    position: absolute; left: 0; top: 0; width: 100%; height: 526px;
    background:
      radial-gradient(ellipse at 0% 40%, rgba(90,160,60,0.35) 0%, transparent 30%),
      radial-gradient(ellipse at 50% 100%, rgba(90,160,60,0.35) 0%, transparent 35%),
      radial-gradient(ellipse at 100% 60%, rgba(90,160,60,0.25) 0%, transparent 25%),
      radial-gradient(ellipse at 0% 0%, rgba(90,160,60,0.3) 0%, transparent 20%);
  }
  .perks-banner { position: absolute; left: 0; top: 0; }
  .card-back .brand-lockup {
    position: absolute; left: 12px; top: 42px; width: 80px;
    display: flex; flex-direction: column; align-items: center; gap: 6px;
  }
  .card-back .brand-lockup .brand-mark { width: 18px; height: 18px; }
  .card-back .brand-lockup .brand-name { font-size: 13px; }
  .perks-title {
    position: absolute; left: 150px; width: 290px; top: 38px;
    text-align: center;
    font-family: "Kaushan Script", cursive;
    font-size: 31px; line-height: 32px; color: var(--magenta);
  }
  .perk-number {
    position: absolute; left: 34px;
    font-size: 30px; font-weight: 700; color: var(--number-red);
  }
  .perk-number--1 { top: 176px; }
  .perk-number--2 { top: 328px; }
  .perk-box {
    position: absolute; left: 89px; width: 336px;
    border-radius: 14px;
    background: linear-gradient(160deg, var(--green-light) 0%, #3e8560 45%, var(--green-dark) 100%);
    color: var(--white);
    font-family: "Kalam", cursive; font-size: 13.4px; line-height: 20.5px;
    padding: 8px 12px;
  }
  .perk-box--loyalty { top: 174px; height: 125px; text-align: center; }
  .perk-box--referral { top: 325px; height: 126px; }
  .perk-box .perk-name { font-size: 16px; font-weight: 700; }
  .loyalty-link {
    position: absolute; left: 84px; top: 456px; width: 345px;
    font-family: "Playfair Display", serif; font-style: italic; font-weight: 700;
    font-size: 11.7px; color: var(--number-red); text-decoration: underline; white-space: nowrap;
  }
  .contact-bar {
    position: absolute; left: 0; top: 526px; width: 446px; height: 144px;
    background: var(--charcoal);
  }
  .contact-list { list-style: none; position: absolute; left: 68px; top: 16px; }
  .contact-item {
    display: flex; align-items: center; height: 44px;
    color: var(--cyan); font-size: 14.5px;
  }
  .contact-icon { width: 28px; height: 28px; margin-right: 32px; }
  .contact-bar .brand-lockup {
    position: absolute; left: 292px; top: 36px; width: 128px;
    display: flex; flex-direction: column; align-items: center; gap: 8px;
  }
  .contact-bar .brand-mark { width: 24px; height: 24px; background: var(--white); }
  .contact-bar .brand-name { color: var(--white); font-size: 18px; }
</style>
</head>
<body>
  <span class="side-label side-label--front">front</span>
  <span class="side-label side-label--back">back</span>

  <section class="card-front" aria-label="Welcome card, front">
    <div class="offer-panel">
      <div class="brand-lockup">
        <span class="brand-mark"></span>
        <span class="brand-name">LeafHarbor</span>
      </div>
      <p class="offer-headline">Save 15% off your<br>next purchase</p>
      <div class="pill pill--code">discount code</div>
      <p class="valid-label">valid until</p>
      <div class="pill pill--date">dd/mm/yy</div>
    </div>
    <div class="hero">
      <div class="hero-photo" role="img" aria-label="Close-up photo of a cannabis flower, green leaves above and pink-violet trichome-covered bud below"></div>
      <svg class="hero-band" width="461" height="435" viewBox="0 0 461 435" aria-hidden="true">
        <polygon points="0,0 461,0 461,225 230,266 0,219" fill="#0d1a0a" fill-opacity="0.5"/>
      </svg>
      <div class="hero-frame"></div>
      <h1 class="hero-title">
        <span class="line-1">Welcome to the</span>
        <span class="line-2">LHR family</span>
      </h1>
    </div>
  </section>

  <section class="card-back" aria-label="Welcome card, back">
    <div class="leaf-pattern" role="img" aria-label="Scattered green cannabis leaf pattern across the background"></div>
    <svg class="perks-banner" width="446" height="170" viewBox="0 0 446 170" aria-hidden="true">
      <polygon points="146,0 446,0 446,135 93,160" fill="var(--charcoal)"/>
    </svg>
    <div class="brand-lockup">
      <span class="brand-mark"></span>
      <span class="brand-name">LeafHarbor</span>
    </div>
    <h2 class="perks-title">Perks of being a part<br>of the family</h2>

    <span class="perk-number perk-number--1">1</span>
    <p class="perk-box perk-box--loyalty"><span class="perk-name">Loyalty Program</span> "Once you've made 5 orders with us you'll be able to join our Loyalty Program! You’ll receive 2.5% back in points with every order to use towards a future purchase. So go ahead, indulge. You deserve it!"</p>

    <span class="perk-number perk-number--2">2</span>
    <p class="perk-box perk-box--referral"><span class="perk-name">Referral Program</span> – Refer a friend using your customer number and they will receive $25 off their first purchase with us AND you'll also receive $25 for your next purchase! Get the full details and customer number at</p>
    <p class="loyalty-link">https://www.leafharbor-shop.example/loyalty/</p>

    <footer class="contact-bar">
      <ul class="contact-list">
        <li class="contact-item">
          <svg class="contact-icon" viewBox="0 0 28 28" aria-label="Website"><rect x="4" y="5" width="20" height="14" rx="1" fill="none" stroke="#fff" stroke-width="2"/><line x1="8" y1="10" x2="20" y2="10" stroke="#fff" stroke-width="1.5"/><line x1="8" y1="14" x2="20" y2="14" stroke="#fff" stroke-width="1.5"/><line x1="14" y1="19" x2="14" y2="23" stroke="#fff" stroke-width="2"/><line x1="9" y1="23" x2="19" y2="23" stroke="#fff" stroke-width="2"/></svg>
          leafharbor-shop.example
        </li>
        <li class="contact-item">
          <svg class="contact-icon" viewBox="0 0 28 28" aria-label="Phone"><path d="M8 5 L12 9 L10 12 C11 15 13 17 16 18 L19 16 L23 20 L20 23 C12 23 5 16 5 8 Z" fill="none" stroke="#fff" stroke-width="1.6" stroke-linejoin="round"/><path d="M16 8 A5 5 0 0 1 20 12" fill="none" stroke="#fff" stroke-width="1.4"/><path d="M16 4 A9 9 0 0 1 24 12" fill="none" stroke="#fff" stroke-width="1.4"/></svg>
          1-833-555-LEAF
        </li>
        <li class="contact-item">
          <svg class="contact-icon" viewBox="0 0 28 28" aria-label="Social profile"><circle cx="14" cy="14" r="11" fill="none" stroke="#fff" stroke-width="1.6"/></svg>
          leafharbor_nth
        </li>
      </ul>
      <div class="brand-lockup">
        <span class="brand-mark"></span>
        <span class="brand-name">LeafHarbor</span>
      </div>
    </footer>
  </section>
</body>
</html>
```